Maple Harbor Home Care Business Cards

We are looking to create double sided, sleek business cards for our new Home Health Care Agency, Maple Harbor Home Care, located in NJ. We want to appear established, professional and at the same time, stand out with a creative and original flair. It should have a luxurious, exclusive feel to it.
The theme colors from our logo should be incorporated into the project.

Our Logo is attached.

Information to be included on the business cards:

Insert Phone Icon: (555)-403-2297
Insert Website Icon: mhhcxq.example
Insert E-mail Icon: info@mhhcxq.example

Follow us on Social Media!
Insert Facebook Icon: (I will provide the link at a later time)
Insert Instagram Icon (I will provide the link at a later time)

In regard to location, we service the areas of: Bayville
Beachwood
Brick
Deal
Howell
Island Heights
Jackson
Lakehurst
Lakewood
Manchester Township
Point Pleasant Beach
Roosevelt
Long Branch
Toms River

All all it's neighboring areas.

However, that can take up a lot of room...therefore, I had in mind to use the backside of the card to have a MAP with all these areas marked on there...in addition to listing these service locations below the map.

We want the card to appear lively and vibrant.

Please note: I will provide the potential winner with the contact's name later on in the process.

A sample idea is attached below as well.

Use your creative juices!

Good luck!

• A map of our service areas on the back of the double sided card.
Sleek design
Our logo (refer to attachment below)

```html
<!DOCTYPE html>
<html lang="en">
<head>
<meta charset="utf-8">
<title>Maple Harbor Home Care – Business Cards</title>
<link rel="stylesheet" href="https://fonts.googleapis.com/css2?family=Montserrat:wght@400;500;700&family=Arimo:wght@400&display=swap">
<style>
  :root {
    --navy: #1752a3;
    --navy-deep: #0f4794;
    --green: #7dc142;
    --grey: #6f6f6f;
    --paper: #ffffff;
    --stage: #e4e4e4;
  }
  * { box-sizing: border-box; margin: 0; padding: 0; }
  html, body { width: 1200px; height: 801px; overflow: hidden; }
  body {
    background: var(--stage);
    font-family: "Montserrat", sans-serif;
    position: relative;
  }
  .card {
    position: absolute;
    top: 246px;
    width: 540px;
    height: 309px;
    box-shadow: 0 6px 18px rgba(0,0,0,0.18);
  }
  /* ---------- front ---------- */
  .card-front {
    left: 40px;
    background: var(--paper);
    border-bottom: 3px solid var(--navy);
  }
  .front-brand {
    position: absolute;
    left: 28px;
    top: 0;
    bottom: 0;
    width: 250px;
    display: flex;
    flex-direction: column;
    align-items: center;
    justify-content: center;
  }
  .brand-mark {
    width: 56px; height: 56px;
    border-radius: 50%;
    border: 5px solid var(--green);
    margin-bottom: 12px;
  }
  .brand-name {
    color: var(--navy);
    font-weight: 700;
    font-size: 20px;
    letter-spacing: 0.5px;
    text-transform: uppercase;
    text-align: center;
    line-height: 1.2;
  }
  .front-divider {
    position: absolute;
    left: 292px; top: 40px;
    width: 2px; height: 228px;
    background: var(--navy);
  }
  .contact {
    position: absolute;
    left: 314px; top: 44px;
    color: var(--grey);
  }
  .contact-name {
    color: var(--navy);
    font-weight: 700;
    font-size: 20px;
    letter-spacing: 0.5px;
  }
  .contact-title { font-size: 14px; margin: 2px 0 14px; }
  .contact-line {
    display: flex; align-items: center; gap: 8px;
    font-size: 13.5px; margin-bottom: 6px;
    white-space: nowrap;
  }
  .contact-line svg { flex: none; }
  .social-heading {
    color: var(--navy);
    font-weight: 700;
    font-size: 12.5px;
    margin: 12px 0 6px;
  }
  .social-dot {
    width: 12px; height: 12px; border-radius: 50%;
    background: var(--green); flex: none;
  }
  /* ---------- back ---------- */
  .card-back {
    left: 620px;
    background: var(--navy-deep);
    color: #fff;
    overflow: hidden;
  }
  .back-map {
    position: absolute;
    left: 40px; top: 20px; right: 20px; height: 200px;
    background: radial-gradient(ellipse at center, rgba(255,255,255,0.10), rgba(255,255,255,0) 70%);
  }
  .back-brand {
    position: absolute;
    left: 0; right: 0; top: 50px;
    display: flex; flex-direction: column; align-items: center;
  }
  .back-brand .brand-mark { width: 64px; height: 64px; }
  .back-brand .brand-name { color: #fff; font-size: 22px; }
  .service-areas {
    position: absolute;
    left: 14px; right: 14px; bottom: 34px;
    font-family: "Arimo", sans-serif;
    font-size: 12.5px;
    line-height: 1.7;
    text-align: center;
  }
  .service-line { display: block; white-space: nowrap; }
  .service-areas .sep { color: var(--green); margin: 0 3px; }
</style>
</head>
<body>

<section class="card card-front" aria-label="Business card front">
  <div class="front-brand">
    <div class="brand-mark"></div>
    <div class="brand-name">Maple Harbor<br>Home Care</div>
  </div>

  <div class="front-divider"></div>

  <div class="contact">
    <div class="contact-name">DANIEL REYES</div>
    <div class="contact-title">President</div>
    <div class="contact-line">
      <svg width="13" height="13" viewBox="0 0 24 24"><path fill="#7dc142" d="M6.6 10.8a15 15 0 0 0 6.6 6.6l2.2-2.2a1 1 0 0 1 1-.25 11.4 11.4 0 0 0 3.6.57 1 1 0 0 1 1 1V20a1 1 0 0 1-1 1A17 17 0 0 1 3 4a1 1 0 0 1 1-1h3.5a1 1 0 0 1 1 1c0 1.25.2 2.45.57 3.6a1 1 0 0 1-.25 1z"/></svg>
      <span>(555)-403-2297</span>
    </div>
    <div class="contact-line">
      <svg width="13" height="13" viewBox="0 0 24 24"><rect x="2" y="5" width="20" height="14" rx="1" fill="#7dc142"/><path d="M2 6l10 7 10-7" stroke="#fff" stroke-width="1.6" fill="none"/></svg>
      <span>info@mhhcxq.example</span>
    </div>
    <div class="contact-line">
      <svg width="13" height="13" viewBox="0 0 24 24"><circle cx="12" cy="12" r="10" fill="none" stroke="#7dc142" stroke-width="2.4"/><path d="M2 12h20M12 2c3 3 3 17 0 20M12 2c-3 3-3 17 0 20" stroke="#7dc142" stroke-width="1.6" fill="none"/></svg>
      <span>www.mhhcxq.example</span>
    </div>
    <div class="social-heading">Follow us on Social Media!</div>
    <div class="contact-line"><span class="social-dot"></span><span>/MapleHarbor</span></div>
    <div class="contact-line"><span class="social-dot"></span><span>@MapleHarbor</span></div>
  </div>
</section>

<section class="card card-back" aria-label="Business card back">
  <div class="back-map" role="img" aria-label="Faint dotted world map pattern behind the company name"></div>
  <div class="back-brand">
    <div class="brand-mark"></div>
    <div class="brand-name">Maple Harbor Home Care</div>
  </div>
  <p class="service-areas">
    <span class="service-line">Beachwood<span class="sep">•</span>Brick<span class="sep">•</span>Deal<span class="sep">•</span>Howell<span class="sep">•</span>Island Heights<span class="sep">•</span>Jackson<span class="sep">•</span>Lakehurst<span class="sep">•</span>Lakewood</span>
    <span class="service-line">Manchester Township<span class="sep">•</span>Point Pleasant Beach<span class="sep">•</span>Roosevelt<span class="sep">•</span>Long Branch<span class="sep">•</span>Toms River</span>
  </p>
</section>

</body>
</html>
```